International Petrochemical business needs a web design for Clearway Desk system

We need a web design for a "Clearway Desk" system for an international petrochemical company. The web site is used internally within the company. It is hosted by an internal department which provides government permit request service for other departments.

We would like to see designs of two pages using color light blue. (home page, internal page as attached).
Home Page:
1. Header has a background image and small animation. Header on home page can be taller than the header of the internal page.
2. Layout as attached.

Internal Page:
1. Header can use the same background image as the home page and can be shorter to utilize the page for content.
2. The blue icon behind every captions represent an icon. When user move mouse over this icon, it displays the caption in Thai language as a tooltip. This icon needs to be redesign.

The final design should communicate the followings:
- Excellent service provided system in terms of time and accurary
- Rapid growth of business via building petrochemical refinery plant

For Internal Page, the blue circle behind every captions represent an icon. When mouse over this icon, a tool tip showing the caption in Thai language is shown. Please also design this icon..

There are more feedbacks from customer as followed:

1. Banner should consists of 
    1.1 "Approved" stamp on paper
    1.2 An image of Garuda. It is used on every government documents in Thailand
    1.3 Image of petrochemical plant
2. Each menu item (Home, Permit, Search, etc) should have different colors. Drop down menu will use the same color as its parent menu item.
3. Overall tone of the web page should be light blue with background of the body the web page in white
4. "New Request" button should use green color with icon on it
5. Table header of each box in the body of the page should use dark blue background with text in white

Please kindly submit your revisions.
Thank you.

Reason: We get some late feedbacks from customers which was just updated to all designers.

• 1. Design for 1024x768 screen resolution
2. Use light blue theme
3. Background of header where the company logo is must have white background

```html
<!DOCTYPE html>
<html lang="en">
<head>
<meta charset="utf-8">
<title>Clearway Desk – Home</title>
<link href="https://fonts.googleapis.com/css2?family=Signika:wght@400;600&family=Nunito:wght@400;600;700&display=swap" rel="stylesheet">
<style>
:root{
  --navy:#25246f;
  --red:#ec2633;
  --cyan:#00aeef;
  --sky:#2fa6ea;
  --ink:#1e1d5c;
  --text:#555;
  --rule:#d9d9d9;
}
*{box-sizing:border-box;margin:0;padding:0}
html,body{width:1073px;height:1200px;overflow:hidden}
body{
  position:relative;
  font-family:"Nunito",sans-serif;
  color:var(--text);
  background:linear-gradient(#fff 0,#fff 120px,#f2f2f2 380px,#f4f4f4 520px,#fff 760px,#fff 1194px,#d7d7d7 1194px);
}
.brand{position:absolute;display:flex;align-items:center;gap:5px;font-weight:700;color:var(--cyan);font-size:11px;line-height:1.15;letter-spacing:.2px}
.brand-dot{width:16px;height:16px;border-radius:50%;background:var(--cyan)}
.brand--top{left:135px;top:36px}
.brand--foot{left:833px;top:1155px}
.product{position:absolute;left:318px;top:37px;color:var(--red);font-size:15px;font-weight:600}

.mainnav{position:absolute;left:124px;top:78px;width:503px;height:38px;border-top:1px dotted #ccc;border-bottom:1px dotted #ccc}
.mainnav a{font-size:13px;font-weight:700;color:var(--cyan);text-decoration:none;letter-spacing:.4px;position:absolute;top:9px}
.mainnav a.is-active{left:0;top:0;width:75px;height:36px;background:var(--navy);color:#fff;display:flex;align-items:center;justify-content:center}
.mainnav .sep{position:absolute;top:9px;height:16px;border-left:1px dotted #bbb}

.hero-art{position:absolute;left:122px;top:140px;width:826px;height:240px;
  background:linear-gradient(180deg,rgba(0,174,239,0) 0%,rgba(0,174,239,.12) 55%,rgba(0,174,239,.45) 88%,#17a9ea 100%)}

.headline{position:absolute;left:132px;top:407px;font-family:"Signika",sans-serif;letter-spacing:-.5px;line-height:1;font-weight:400}
.headline .l1{font-size:24px;color:#555;display:block}
.headline .l2{font-size:27px;font-weight:600;color:var(--navy);display:block;margin-top:3px}
.headline .dark{color:var(--navy)}
.headline .hot{color:var(--red)}

.panel{position:absolute;background:#fff;border:1px solid var(--rule);border-radius:4px;box-shadow:0 2px 3px rgba(0,0,0,.06);overflow:hidden}
.panel-title{height:43px;display:flex;align-items:center;padding-left:11px;font-family:"Signika",sans-serif;font-weight:600;font-size:21px;color:#fff;letter-spacing:-.4px}
.panel--navy .panel-title{background:var(--navy)}
.panel--red .panel-title{background:var(--red)}
.panel--sky .panel-title{background:var(--sky);height:31px;font-size:17px;font-weight:400;padding-left:17px}

.grid{width:100%;border-collapse:collapse;table-layout:fixed;font-size:13px}
.grid th{font-size:13px;font-weight:600;color:var(--ink);text-align:left;padding-left:11px;height:36px;border-bottom:1px dotted var(--rule);letter-spacing:.2px}
.grid td{height:35px;border-bottom:1px dotted var(--rule);text-align:center;color:var(--text)}
.grid th+th,.grid td+td{border-left:1px solid #e6e6e6}
.grid td.left{text-align:left;padding-left:22px}
.grid--band{font-size:13.5px}
.grid--band th{background:var(--cyan);color:#fff;font-weight:600;font-size:13.5px;height:34px;padding-left:22px;border:0}
.grid--band td{height:38px;text-align:left;padding-left:22px}

.pager{position:absolute;right:16px;bottom:10px;display:flex;gap:3px;font-size:9px}
.pager span{width:13px;height:13px;background:#e3e3e3;color:#999;display:flex;align-items:center;justify-content:center}
.pager span.is-current{background:var(--navy);color:#fff}
.pager span.arrow{background:#e8e8e8;color:#666;font-size:10px}

.cta{position:absolute;left:566px;top:902px;width:382px;height:62px;background:var(--red);border-radius:4px;display:flex;align-items:center;padding-left:22px;color:#fff;font-family:"Signika",sans-serif;font-weight:600;font-size:29px;letter-spacing:-.5px;text-decoration:none}
.cta svg.doc{margin-right:14px}
.cta .go{position:absolute;right:16px;top:14px;width:34px;height:34px;border-radius:50%;background:#fff;display:flex;align-items:center;justify-content:center}

.footer-rule{position:absolute;left:124px;top:1128px;width:826px;border-top:1px dotted #ccc}
.copyright{position:absolute;left:128px;top:1147px;font-size:12px;color:#888}
</style>
</head>
<body>

<div class="brand brand--top"><span class="brand-dot"></span>NORVANE<br>PETROCHEMICAL</div>
<div class="product">Clearway Desk</div>

<nav class="mainnav">
  <a class="is-active" href="#">HOME</a>
  <a href="#" style="left:92px">PERMITS</a><span class="sep" style="left:170px"></span>
  <a href="#" style="left:191px">SEARCH</a><span class="sep" style="left:259px"></span>
  <a href="#" style="left:281px">REPORT</a><span class="sep" style="left:352px"></span>
  <a href="#" style="left:379px">ADMIN</a><span class="sep" style="left:445px"></span>
  <a href="#" style="left:471px">HELP</a>
</nav>

<div class="hero-art" role="img" aria-label="Banner illustration: blue oil drilling rigs and refinery skyline over a faint world map"></div>

<h1 class="headline">
  <span class="l1"><span class="dark">CLEARWAY DESK</span> SYSTEM FOR AN</span>
  <span class="l2">INTERNATIONAL <span class="hot">PETROCHEMICAL COMPANY</span></span>
</h1>

<section class="panel panel--navy" style="left:124px;top:480px;width:407px;height:178px">
  <h2 class="panel-title">NEW REQUESTS</h2>
  <table class="grid">
    <colgroup><col style="width:105px"><col style="width:147px"><col></colgroup>
    <tr><th>Request No.</th><th style="padding-left:22px">Requested Date</th><th style="padding-left:22px">Branch</th></tr>
    <tr><td>56-0003</td><td>20/4/2013</td><td class="left" style="padding-left:33px">GC1</td></tr>
    <tr><td>56-0004</td><td>21/4/2013</td><td class="left" style="padding-left:33px">GC2</td></tr>
  </table>
  <div class="pager"><span class="arrow">«</span><span class="is-current">1</span><span>2</span><span>3</span><span>4</span><span class="arrow">»</span></div>
</section>

<section class="panel panel--red" style="left:541px;top:480px;width:407px;height:178px">
  <h2 class="panel-title">MY WORKING REQUESTS</h2>
  <table class="grid">
    <colgroup><col style="width:106px"><col style="width:146px"><col></colgroup>
    <tr><th>Request No.</th><th style="padding-left:21px">Requested Date</th><th style="padding-left:22px">Status</th></tr>
    <tr><td>55-0200</td><td>25/3/2013</td><td class="left">Waiting for process</td></tr>
    <tr><td>55-0210</td><td>23/3/2013</td><td class="left">In progress</td></tr>
  </table>
  <div class="pager"><span class="arrow">«</span><span class="is-current">1</span><span>2</span><span>3</span><span>4</span><span class="arrow">»</span></div>
</section>

<section class="panel panel--navy" style="left:124px;top:688px;width:824px;height:180px">
  <h2 class="panel-title" style="height:37px">EXPIRING PERMITS</h2>
  <table class="grid grid--band">
    <colgroup><col style="width:105px"><col style="width:132px"><col style="width:163px"><col style="width:124px"><col style="width:167px"><col></colgroup>
    <tr><th>Permit No.</th><th>Expire Date</th><th>Permit Name</th><th>Branch</th><th>Required Time (Day)</th><th>Due Date</th></tr>
    <tr><td>56-0003</td><td>20/4/2013</td><td>Permit Name ###10</td><td>GC1</td><td>30 Days</td><td>- 40 Days</td></tr>
    <tr><td>56-0004</td><td>21/4/2013</td><td>Permit Name ###10</td><td>GC2</td><td>60 Days</td><td>- 15 Days</td></tr>
  </table>
  <div class="pager"><span class="arrow">«</span><span class="is-current">1</span><span>2</span><span>3</span><span>4</span><span class="arrow">»</span></div>
</section>

<section class="panel panel--navy" style="left:124px;top:902px;width:429px;height:202px">
  <h2 class="panel-title" style="height:34px">MY IN PROGRESS REQUESTS</h2>
  <table class="grid">
    <colgroup><col style="width:110px"><col style="width:147px"><col></colgroup>
    <tr><th style="padding-left:15px">Request No.</th><th style="padding-left:21px">Requested Date</th><th style="padding-left:21px">Status</th></tr>
    <tr><td>56-0001</td><td>20/4/2013</td><td class="left">In progress</td></tr>
    <tr><td>56-0002</td><td>21/4/2013</td><td class="left">In progress</td></tr>
    <tr><td>56-0002</td><td>21/4/2013</td><td class="left">In progress</td></tr>
  </table>
  <div class="pager"><span class="arrow">«</span><span class="is-current">1</span><span>2</span><span>3</span><span>4</span><span class="arrow">»</span></div>
</section>

<a class="cta" href="#">
  <svg class="doc" width="30" height="30" viewBox="0 0 30 30" fill="none" stroke="#fff" stroke-width="2.4" stroke-linejoin="round">
    <path d="M6 3h12l7 7v17H6z"/><path d="M18 3v7h7"/><path d="M3 14l9 9"/>
  </svg>
  NEW REQUESTS
  <span class="go"><svg width="12" height="14" viewBox="0 0 12 14"><path d="M2 1l9 6-9 6z" fill="#111"/></svg></span>
</a>

<section class="panel panel--sky" style="left:566px;top:977px;width:382px;height:127px">
  <h2 class="panel-title">RECENT COMPLETED REQUESTS</h2>
  <table class="grid">
    <colgroup><col style="width:138px"><col></colgroup>
    <tr><th style="padding-left:17px;height:30px">Request No.</th><th style="padding-left:29px;height:30px">Complete Date</th></tr>
    <tr><td class="left" style="padding-left:17px;height:28px">56-0001</td><td class="left" style="padding-left:29px;height:28px">20/4/2013</td></tr>
  </table>
  <div class="pager"><span class="arrow">«</span><span class="is-current">1</span><span>2</span><span>3</span><span>4</span><span class="arrow">»</span></div>
</section>

<div class="footer-rule"></div>
<p class="copyright">Copyright © 2013 Norvane Petrochemical. All rights reserved.</p>
<div class="brand brand--foot"><span class="brand-dot"></span>NORVANE<br>PETROCHEMICAL</div>

</body>
</html>
```